Invitation to Retail Shopping Event

-Must include logo
-Can contain product pictures depending on design
-I prefer any graphics to be my own product pictures
-Should include the following language:
Sip and Shop
Thursday, November 18
11 to 1 pm
478 Fenwick Lane
Come enjoy sips, snacks and shopping! Be the first to preview our new winter collection and get an early start on your holiday gifting.
Please RSVP to 402-319-5577 or info@pelbrika.com

```html
<!DOCTYPE html>
<html lang="en">
<head>
<meta charset="utf-8">
<title>Pelbrika – Sip &amp; Shop</title>
<link rel="stylesheet" href="https://fonts.googleapis.com/css2?family=Arimo:wght@400;700&family=Great+Vibes&display=swap">
<style>
  :root {
    --blush: #e8cdc9;
    --white: #ffffff;
    --slate: #5e5e5e;
    --script: #6a6a6a;
    --rust: #9c5a47;
    --rust-soft: #b27764;
    --body-grey: #555555;
    --tray-gold: #d8b98a;
    --tray-dark: #3a2a1e;
    --gold: #d9b45a;
    --bag: #d6bdb3;
  }
  * { margin: 0; padding: 0; box-sizing: border-box; }
  html, body { width: 800px; height: 1200px; overflow: hidden; background: var(--white); }
  .invite {
    position: relative;
    width: 800px;
    height: 1200px;
    overflow: hidden;
    font-family: "Arimo", Arial, sans-serif;
    background: var(--white);
  }
  .invite__blush {
    position: absolute;
    left: 0; top: 0;
    width: 800px; height: 970px;
    background: var(--blush);
  }
  .brand {
    position: absolute;
    left: 0; top: 138px;
    width: 800px;
    text-align: center;
    font-weight: 700;
    font-size: 62px;
    letter-spacing: 2px;
    color: var(--slate);
  }
  .event-title {
    position: absolute;
    left: 150px; top: 350px;
    width: 500px;
    text-align: center;
    white-space: nowrap;
    font-family: "Great Vibes", cursive;
    font-size: 96px;
    line-height: 1;
    color: var(--script);
    transform: rotate(-24deg);
    transform-origin: center;
  }
  .event-details {
    position: absolute;
    left: 320px; top: 500px;
    width: 420px;
    text-align: center;
    font-size: 27px;
    line-height: 37px;
    color: var(--rust);
  }
  .event-invite {
    position: absolute;
    left: 300px; top: 684px;
    width: 475px;
    text-align: center;
    font-size: 25px;
    line-height: 34px;
    color: var(--rust-soft);
  }
  .preview-note {
    position: absolute;
    left: 80px; top: 995px;
    width: 380px;
    text-align: center;
    font-size: 21px;
    line-height: 28px;
    color: var(--body-grey);
  }
  .rsvp {
    position: absolute;
    left: 80px; top: 1120px;
    width: 380px;
    text-align: center;
    font-size: 18px;
    line-height: 25px;
    color: var(--body-grey);
  }
  .product {
    position: absolute;
  }
  .product--tray {
    left: -170px; top: 398px;
    width: 412px; height: 412px;
    border-radius: 50%;
    background: radial-gradient(circle at 55% 50%, var(--tray-gold) 0%, #b89a6e 60%, var(--tray-dark) 100%);
  }
  .product--earrings {
    left: 668px; top: 178px;
    width: 132px; height: 312px;
    border-radius: 60px 0 0 60px;
    background: linear-gradient(180deg, var(--gold), #c7a24e 50%, var(--gold));
    opacity: 0.55;
  }
  .product--tote {
    left: 480px; top: 800px;
    width: 320px; height: 400px;
    border-radius: 40px 0 0 0;
    background: linear-gradient(160deg, #e0cbc2, var(--bag) 60%, #c7aca1);
  }
</style>
</head>
<body>
  <main class="invite">
    <div class="invite__blush"></div>

    <div class="brand">PELBRIKA</div>

    <div class="product product--earrings" role="img" aria-label="Product photo: pair of gold beaded flower earrings with crystal centres"></div>

    <div class="event-title">Sip &amp; Shop</div>

    <div class="product product--tray" role="img" aria-label="Product photo: round leopard-print lacquered tray with gold rim"></div>

    <div class="event-details">
      <p>THURSDAY, NOVEMBER 18</p>
      <p>11 TO 1 PM</p>
      <p>478 FENWICK LANE</p>
    </div>

    <div class="event-invite">
      <p>COME ENJOY</p>
      <p>SIPS, SNACKS AND SHOPPING!</p>
    </div>

    <p class="preview-note">Be the first to preview our new winter collection and get an early start on your holiday gifting.</p>

    <p class="rsvp">Please RSVP to 402-319-5577<br>or info@pelbrika.com</p>

    <div class="product product--tote" role="img" aria-label="Product photo: blush leather tote bag with a painted blue snake motif"></div>
  </main>
</body>
</html>
```